Digital multi-page Product Brochure

We’re creating a product brochure for our Wood Look Porcelain Pavers. The brochure will show technical details of the pavers, available colors, and applications while also showcasing the advantages of porcelain over wood.
We prefer a clean design aesthetic with appropriate white space incorporated. Because we want the view to appreciate the detail and natural look of the porcelain pavers, we want relatively large color swatches in the available colors section.
Each color swatch section needs the information provided in the guide. The design and layout of these sections is completely open. We do want to see a visual of the paver size in each color swatch section along with the written sizing information.
Mixed use of renderings and actual installation photos. Style and placement of photos is up to designer.
Target Market(s)
Architects and contractors
Industry/Entity Type
Building Materials
Font styles to use
Other font styles liked:
- Outfit - headers, Helvetica for paragraph copy

```html
<!DOCTYPE html>
<html lang="en">
<head>
<meta charset="utf-8">
<title>Terravia Porcelain Pavers – Brochure Spreads</title>
<link rel="stylesheet" href="https://fonts.googleapis.com/css2?family=Outfit:wght@400;500&family=Arimo:wght@400;700&display=swap">
<style>
  :root{
    --teal:#0e7c86;
    --teal-light:#2aa3b1;
    --ink:#222;
    --muted:#666;
    --rule:#ddd;
    --paper:#fff;
    --bg:#fff;
    --wood-dark:#5e5247;
    --wood-mid:#7d6e60;
    --wood-light:#a8998a;
    --orange:#c8732f;
  }
  *{box-sizing:border-box;margin:0;padding:0}
  html,body{width:1200px;height:848px;overflow:hidden;background:var(--bg)}
  body{position:relative;font-family:Arimo,Helvetica,Arial,sans-serif;color:var(--ink)}
  .page{position:absolute;width:253px;height:327px;background:var(--paper);overflow:hidden;box-shadow:0 0 0 1px #eee}
  .p1{left:80px;top:92px}.p2{left:344px;top:92px}.p3{left:607px;top:92px}.p4{left:869px;top:92px}
  .p5{left:80px;top:431px}.p6{left:344px;top:431px}.p7{left:607px;top:431px}.p8{left:869px;top:431px}

  .brand{position:absolute;left:16px;top:13px;display:flex;align-items:center;gap:4px;font-family:Outfit,sans-serif;font-size:13px;font-weight:400;color:var(--ink);z-index:3}
  .brand .mark{width:8px;height:8px;background:var(--teal)}
  .brand.on-photo{color:#fff}
  .brand.on-photo .mark{background:#fff}

  .band{position:absolute;left:33px;top:33px;width:190px;height:19px;background:var(--teal);color:#fff;font-family:Outfit,sans-serif;font-size:12px;font-weight:400;text-align:center;line-height:19px;letter-spacing:.2px;z-index:3}

  .box{position:absolute;border:1.3px solid var(--teal);padding:9px 4px 4px 4px;font-size:6.3px;line-height:1.3;color:var(--ink);z-index:2}
  .box-title{position:absolute;top:-7px;left:4px;background:var(--paper);padding:0 4px;font-family:Outfit,sans-serif;font-size:9px;color:var(--teal-light);white-space:nowrap;line-height:12px}
  .box ul{list-style:none}
  .box li{position:relative;padding-left:6px;margin-bottom:4px}
  .box li::before{content:"•";position:absolute;left:0}
  .box p{margin-bottom:3px}
  .figure{position:absolute;background:#f2f4f5;border:1px solid #e3e6e8}
  .legend{position:absolute;font-size:4.6px;line-height:1.5;color:#333}

  .photo{position:absolute}

  /* Page 1 */
  .p1 .bg{left:0;top:0;width:253px;height:327px;background:linear-gradient(180deg,#fff 0%,#f3f3f3 18%,#cfd3d4 45%,#9b8a79 78%,#6d5c4b 100%)}
  .p1 .box{left:43px;top:66px;width:167px;height:99px;padding:8px 4px 3px 4px;font-size:6px;line-height:1.24;background:rgba(255,255,255,.82)}
  .p1 .box p{margin-bottom:2px}
  .p1 .box-title{background:#f6f6f6}

  /* Page 2 */
  .p2 .ph-a{left:0;top:0;width:126px;height:327px;background:linear-gradient(180deg,#5a3a33 0%,#6e4d42 40%,#8a8475 70%,#4e4239 100%)}
  .p2 .ph-b{left:127px;top:0;width:126px;height:108px;background:linear-gradient(180deg,#8a8f94,#6e675d)}
  .p2 .ph-c{left:127px;top:109px;width:126px;height:108px;background:linear-gradient(135deg,#b8b2aa,#8e877d)}
  .p2 .ph-d{left:127px;top:218px;width:126px;height:109px;background:linear-gradient(135deg,#a07b5a,#cdb9a1)}

  /* Page 6 table */
  .spec-sub{color:var(--orange);font-size:4.2px;margin-bottom:5px}
  table.spec{width:162px;border-collapse:collapse;font-size:3.2px;color:#555}
  table.spec th{text-align:left;font-weight:700;color:#333;padding:1.4px 2px;border-bottom:.5px solid var(--rule)}
  table.spec td{padding:1.4px 2px;border-bottom:.5px solid var(--rule)}
  table.spec td:first-child{font-weight:700;color:#444}
  table.spec td:nth-child(2),table.spec th:nth-child(2),
  table.spec td:nth-child(3),table.spec th:nth-child(3){text-align:center}
  .spec-tab{position:absolute;right:3px;top:8px;width:13px;height:62px;background:var(--orange);color:#fff;font-size:3.6px;writing-mode:vertical-rl;padding:3px 1px;clip-path:polygon(0 0,100% 0,100% 100%,0 88%)}
  .spec-note{font-size:2.9px;line-height:1.35;color:#444;margin-top:5px;font-weight:700}

  /* Page 7 swatches */
  .swatch{position:absolute;background:linear-gradient(90deg,var(--wood-dark),var(--wood-mid) 45%,var(--wood-dark) 70%,var(--wood-mid))}
  .label{font-size:6.3px}

  /* Page 8 */
  .p8 .ph-gallery{left:0;top:125px;width:253px;height:202px;background:linear-gradient(180deg,#b9cde0 0%,#dfe7ec 30%,#7c8d6a 60%,#5f7a3e 80%,#8d7a66 100%)}
  .p8 .box b{font-weight:700}
</style>
</head>
<body>

<!-- Applications -->
<section class="page p1">
  <div class="photo bg" role="img" aria-label="Rendering of a rooftop terrace with wood-look porcelain pavers, glass pavilion and green chairs"></div>
  <div class="brand"><span class="mark"></span>Terravia</div>
  <div class="band">APPLICATIONS</div>
  <div class="box">
    <span class="box-title">Rooftop decks, patios, and terraces</span>
    <p>Create outdoor surfaces with elegance and style for rooftop bars, restaurants, swimming pools, outdoor lounges and other social gathering spaces.</p>
    <p>The only currently available solution for totally <b>non-combustible roof decks</b> that won’t catch fire, burn, emit smoke, or lose their structural integrity.</p>
    <p>Terravia porcelain pavers installed on Pyrocore steel pedestals <b>meet Class A fire rating</b> requirements for all components – both deck surface and structural supports.</p>
  </div>
</section>

<!-- Installation options collage -->
<section class="page p2">
  <div class="photo ph-a" role="img" aria-label="Brick apartment building with a paved terrace lounge and fire table"></div>
  <div class="photo ph-b" role="img" aria-label="Rooftop terrace with outdoor dining furniture"></div>
  <div class="photo ph-c" role="img" aria-label="Lounge sofas and square fire pit on grey wood-look pavers"></div>
  <div class="photo ph-d" role="img" aria-label="Interior room with herringbone wood-look porcelain floor"></div>
  <div class="brand on-photo"><span class="mark"></span>Terravia</div>
  <div class="band">INSTALLATION OPTIONS</div>
</section>

<!-- Pedestals -->
<section class="page p3">
  <div class="brand"><span class="mark"></span>Terravia</div>
  <div class="band">INSTALLATION OPTIONS</div>
  <div class="box" style="left:32px;top:69px;width:190px;height:94px">
    <span class="box-title">Elevated on Adjustable Height Pedestals</span>
    <ul>
      <li>For elevated decks on rooftops and other hard, stable surfaces with deck heights up to 30” or more.</li>
      <li>Adjustable height pedestals are placed under each corner of the pavers and sides where lengths exceed 24”.</li>
    </ul>
    <div class="legend" style="left:3px;top:55px">1. Porcelain planks<br>2. Sliding head<br>3. Steel rail<br>4. Adjustable height<br>&nbsp;&nbsp;&nbsp;pedestals</div>
    <div class="figure" role="img" aria-label="Section drawing of planks on sliding heads, steel rail and adjustable pedestals" style="left:52px;top:54px;width:132px;height:34px"></div>
  </div>
  <div class="box" style="left:32px;top:183px;width:190px;height:110px">
    <span class="box-title">Elevated on Pedestal Supported Rails</span>
    <ul>
      <li>For elevated decks on rooftops and other hard, stable Surfaces with plank style pavers, 16” or less in width.</li>
      <li>8’ long steel rails are laid over adjustable height pedestals.</li>
      <li>Pavers are laid on sliding heads at each corner and along sides at intervals not exceeding 24”.</li>
    </ul>
    <div class="legend" style="left:3px;top:70px">1. Porcelain planks<br>2. Sliding head<br>3. Steel rail<br>4. Adjustable height<br>&nbsp;&nbsp;&nbsp;pedestals</div>
    <div class="figure" role="img" aria-label="Section drawing of planks on steel rails over adjustable pedestals" style="left:52px;top:69px;width:132px;height:34px"></div>
  </div>
</section>

<!-- Pads & gravel -->
<section class="page p4">
  <div class="brand"><span class="mark"></span>Terravia</div>
  <div class="band">INSTALLATION OPTIONS</div>
  <div class="box" style="left:28px;top:69px;width:190px;height:94px">
    <span class="box-title">Elevated on Fixed Height Rubber Pads</span>
    <ul>
      <li>For existing concrete resurfacing at elevations less than 1.5”.</li>
      <li>Pads are placed under each corner of the pavers and stacked as required to ensure a level surface.</li>
      <li>Shims provide minor height adjustment and prevent rocking.</li>
    </ul>
    <div class="legend" style="left:3px;top:58px">1. Porcelain planks<br>2. Fixed height<br>&nbsp;&nbsp;&nbsp;rubber pads<br>3. Concrete base</div>
    <div class="figure" role="img" aria-label="Section drawing of planks on rubber pads over a concrete base" style="left:52px;top:54px;width:132px;height:33px"></div>
  </div>
  <div class="box" style="left:28px;top:183px;width:190px;height:110px">
    <span class="box-title">Dry Installation on Sand/Gravel Beds</span>
    <ul>
      <li>For broad area landscaping, plazas, terraces.</li>
      <li>Pavers are laid directly over a well compacted base of crushed rock and sand.</li>
    </ul>
    <div class="figure" role="img" aria-label="Section drawing of pavers over sand, gravel and crushed rock with a restraining barrier" style="left:28px;top:44px;width:132px;height:58px"></div>
  </div>
</section>

<!-- Thinset -->
<section class="page p5">
  <div class="brand"><span class="mark"></span>Terravia</div>
  <div class="band">INSTALLATION OPTIONS</div>
  <div class="box" style="left:33px;top:71px;width:190px;height:136px">
    <span class="box-title">Thinset &amp; Grout Over Concrete Slabs</span>
    <ul>
      <li>For vehicular and high traffic on-grade landscaping and walkways.</li>
      <li>Pavers are laid with mortar or approved adhesive over are inforced concrete base and grouted.</li>
      <li>Transition to adjustable height pedestals at heights exceeding 1.5”.</li>
    </ul>
    <div class="figure" role="img" aria-label="Section drawing of pavers on thinset mortar over gravel mixed with cement, sand and soil" style="left:30px;top:72px;width:118px;height:56px"></div>
  </div>
</section>

<!-- Technical data -->
<section class="page p6">
  <div class="brand"><span class="mark"></span>Terravia</div>
  <div class="band">TECHNICAL DATA</div>
  <div class="box" style="left:28px;top:62px;width:202px;height:218px;padding:6px 6px 4px 7px">
    <span class="box-title" style="font-size:6px;color:var(--ink);top:-5px;line-height:9px"><b style="font-family:Outfit,sans-serif;font-weight:500">▪ Terravia</b> <span style="color:var(--orange);font-family:Outfit,sans-serif">Porcelain Pavers</span></span>
    <div class="spec-tab">SPECIFICATIONS · Technical Characteristics</div>
    <div class="spec-sub" style="margin-top:4px">Technical Characteristics</div>
    <table class="spec">
      <tr><th>CHARACTERISTIC</th><th>TEST METHOD</th><th>VALUE*</th></tr>
      <tr><td>Thickness</td><td></td><td>3/4"</td></tr>
      <tr><td>Weight</td><td></td><td>9 lb/sq.ft</td></tr>
      <tr><td>Water absorption</td><td>ISO 10545-3</td><td>&lt;0.1%</td></tr>
      <tr><td>Breaking strength</td><td>ISO 10545-4</td><td>&gt;2200 lbf</td></tr>
      <tr><td>Modulus of rupture</td><td>ISO 10545-4</td><td>&gt;7000 psi</td></tr>
      <tr><td>Static load capacity*</td><td>EN 12825</td><td>&gt;1700 lbf</td></tr>
      <tr><td>Bending strength</td><td>EN 1339</td><td>Class 14</td></tr>
      <tr><td>Impact resistance</td><td>ISO 10545-5</td><td>&gt;0.55</td></tr>
      <tr><td>Resistance to abrasion</td><td>ISO 10545-6</td><td>conforms</td></tr>
      <tr><td>Frost resistant</td><td>ISO 10545-12</td><td>resistant</td></tr>
      <tr><td>Resistance to thermal shock</td><td>ISO 10545-9</td><td>resistant</td></tr>
      <tr><td>Resistance to chemicals</td><td>ISO 10545-13</td><td>UA</td></tr>
      <tr><td>Resistance to acids &amp; alkalis</td><td>ISO 10545-13</td><td>ULA/UHA</td></tr>
      <tr><td>Resistance to staining</td><td>ISO 10545-14</td><td>Class 5</td></tr>
      <tr><td>Fire Resistance</td><td>EN 13501-1</td><td>A1-A1 FL</td></tr>
      <tr><td>Barefoot ramp test</td><td>DIN 51097</td><td>A+B+C</td></tr>
      <tr><td>Shod ramp test</td><td>DIN 51130</td><td>R11</td></tr>
      <tr><td>Static Coefficient of friction</td><td>ASTM C1028-2007</td><td>&gt;0.6 wet</td></tr>
    </table>
    <div class="spec-note">** 24” x 24” pavers<br>*Average values - compliant with relevant standard<br>*Terravia P20 porcelain pavers are made in several factories. The chart shows typical values across these facilities. Please contact Terravia to confirm specifications for any specific paver color or size.</div>
  </div>
</section>

<!-- Patterns -->
<section class="page p7">
  <div class="brand"><span class="mark"></span>Terravia</div>
  <div class="band">PATTERN AND LAYING IDEAS</div>
  <div class="box" style="left:43px;top:69px;width:167px;height:24px;padding-top:7px">
    <span class="box-title">Current Styles</span>
    Do we have anything like this for wood currently?
  </div>
  <div class="box" style="left:43px;top:109px;width:167px;height:98px;padding-top:7px">
    <span class="box-title">Planks</span>
    <div class="label">Stack Bond</div>
    <div class="swatch" role="img" aria-label="Single wood-look plank" style="left:14px;top:21px;width:135px;height:17px"></div>
    <div class="label" style="position:absolute;left:4px;top:47px">Running Bond</div>
    <div class="swatch" role="img" aria-label="Wood-look planks in running bond" style="left:4px;top:61px;width:136px;height:16px"></div>
    <div class="swatch" role="img" aria-label="Second row of running bond planks" style="left:26px;top:78px;width:136px;height:16px"></div>
  </div>
  <div class="box" style="left:43px;top:222px;width:167px;height:83px;padding-top:7px">
    <span class="box-title">Slabs</span>
    <div class="label">Multiple board 24” x 24” slabs</div>
    <div class="swatch" role="img" aria-label="Wood-look multi-board slab" style="left:14px;top:20px;width:56px;height:27px"></div>
    <div class="swatch" role="img" aria-label="Four slabs in alternating basket-weave pattern" style="left:88px;top:20px;width:56px;height:56px;background:conic-gradient(var(--wood-mid) 0 25%,var(--wood-dark) 0 50%,var(--wood-mid) 0 75%,var(--wood-dark) 0)"></div>
  </div>
</section>

<!-- Gallery -->
<section class="page p8">
  <div class="brand"><span class="mark"></span>Terravia</div>
  <div class="band">PROJECT GALLERY</div>
  <div class="box" style="left:42px;top:69px;width:167px;height:49px;padding-top:8px;font-size:6.3px">
    <span class="box-title">Civic Heritage Museum</span>
    <p style="margin-bottom:2px"><b>Location:</b> Washington DC</p>
    <p style="margin-bottom:2px"><b>Architects:</b> Marlow Pike Architects</p>
    <p style="margin-bottom:2px"><b>Style:</b> 16” x 48” Plank</p>
    <p><b>Color:</b> Oak</p>
  </div>
  <div class="photo ph-gallery" role="img" aria-label="Photo of a green roof terrace with wood-look plank walkway, glass pavilion and river view"></div>
</section>

</body>
</html>
```